"Copper Hollow" Moonshine 6-Pack Shipper Design

We're looking for a 6-pack shipper design for our moonshine brand - "Copper Hollow". We're looking for a classic look printed with black ink on regular uncoated cardboard.

Attached are a couple examples, the die line that the file will need to be designed within, and our brand label artwork to be used.

Thank you!

```html
<!DOCTYPE html>
<html lang="en">
<head>
<meta charset="utf-8">
<title>Copper Hollow 6-Pack Shipper Dieline</title>
<link rel="stylesheet" href="https://fonts.googleapis.com/css2?family=Rye&family=Oswald:wght@400;500&family=Montserrat:wght@500;700;800&family=Roboto:wght@700&display=swap">
<style>
  :root {
    --kraft: #cc9f76;
    --kraft-light: #d3a880;
    --ink: #141414;
    --dim-blue: #0a84c6;
    --cut-red: #e0242b;
    --edge-gray: #2b2b2b;
    --paper: #ffffff;
  }
  html, body { margin: 0; padding: 0; background: var(--paper); }
  body { width: 1200px; height: 1107px; overflow: hidden; position: relative; }
  .dieline { position: absolute; left: 0; top: 0; width: 1200px; height: 1107px; }
  .cut { stroke: #333; stroke-width: 1; }
  .kraft { fill: var(--kraft); }
  .ink { fill: var(--ink); }
  .fold { fill: none; stroke: var(--cut-red); stroke-width: 0.9; stroke-dasharray: 6 2 1.5 2; }
  .dim-line { stroke: var(--dim-blue); stroke-width: 1; fill: none; }
  .dim-text { font-family: "Roboto", Arial, sans-serif; font-weight: 700; fill: var(--dim-blue); }
  .lead-edge { font-family: "Roboto", Arial, sans-serif; font-weight: 700; font-size: 31px; fill: var(--edge-gray); }
  .name { font-family: "Montserrat", sans-serif; font-weight: 800; }
  .display { font-family: "Rye", serif; }
  .sans { font-family: "Montserrat", sans-serif; font-weight: 700; }
  .condensed { font-family: "Oswald", sans-serif; font-weight: 500; }
  .story {
    position: absolute; left: 606px; top: 505px; width: 92px;
    font-family: "Montserrat", sans-serif; font-weight: 500;
    font-size: 3.7px; line-height: 5.9px; color: var(--kraft); margin: 0;
  }
  .story strong { font-weight: 800; }
  .warning {
    position: absolute; left: 602px; top: 595px; width: 98px;
    font-family: "Oswald", sans-serif; font-weight: 400;
    font-size: 3.1px; line-height: 4.9px; color: var(--kraft);
    text-align: justify; margin: 0; letter-spacing: 0.1px;
  }
  .warning strong { font-weight: 500; }
</style>
</head>
<body>
<svg class="dieline" viewBox="0 0 1200 1107" xmlns="http://www.w3.org/2000/svg">
  <defs>
    <marker id="chevron" viewBox="0 0 14 10" refX="14" refY="5" markerWidth="14" markerHeight="10" markerUnits="userSpaceOnUse" orient="auto-start-reverse">
      <path d="M0,0 L14,5 L0,10" fill="none" stroke="#0a84c6" stroke-width="1.2"/>
    </marker>
    <linearGradient id="woodgrain" x1="0" y1="0" x2="1" y2="1">
      <stop offset="0" stop-color="#d3a880"/>
      <stop offset="0.5" stop-color="#c99b71"/>
      <stop offset="1" stop-color="#cfa37a"/>
    </linearGradient>

    <g id="front-panel">
      <!-- top flap -->
      <rect class="kraft cut" x="291" y="369" width="265" height="92"/>
      <rect class="ink" x="291" y="384" width="265" height="77"/>
      <g class="name" font-size="4.6" fill="#141414" text-anchor="middle">
        <text x="324" y="379">COPPER HOLLOW</text>
        <text x="374" y="379">COPPER HOLLOW</text>
        <text x="423" y="379">COPPER HOLLOW</text>
        <text x="473" y="379">COPPER HOLLOW</text>
        <text x="522" y="379">COPPER HOLLOW</text>
      </g>
      <text class="name" x="423" y="428" font-size="16" fill="#cc9f76" text-anchor="middle" letter-spacing="1">COPPER HOLLOW</text>

      <!-- body -->
      <rect x="287" y="461" width="273" height="222" fill="url(#woodgrain)" role="img" aria-label="Hand-drawn wood grain pattern"/>
      <rect class="ink" x="287" y="461" width="273" height="38"/>
      <rect class="ink" x="389" y="624" width="171" height="54"/>
      <rect class="ink" x="294" y="509" width="93" height="174" role="img" aria-label="Illustration of a moonshine jug silhouette"/>
      <text class="condensed" x="340" y="652" font-size="26" fill="#cc9f76" text-anchor="middle">6 PACK</text>
      <text class="condensed" x="340" y="665" font-size="9" fill="#cc9f76" text-anchor="middle" font-weight="400">750 | 80 | 40%</text>
      <text class="condensed" x="340" y="671" font-size="3.6" fill="#cc9f76" text-anchor="middle" word-spacing="14">ML PROOF ABV</text>

      <rect x="395" y="476" width="152" height="148" fill="#d3a880" role="img" aria-label="Brand label artwork area"/>
      <text class="sans" x="471" y="492" font-size="5.5" fill="#141414" text-anchor="middle" letter-spacing="0.6">CRAFTED IN MILLBROOK, TN</text>
      <text class="name" x="471" y="548" font-size="26" fill="#141414" text-anchor="middle">COPPER</text>
      <text class="name" x="471" y="598" font-size="26" fill="#141414" text-anchor="middle">HOLLOW</text>
      <text x="471" y="617" font-size="6" fill="#141414" text-anchor="middle" letter-spacing="7">★★★★★★★★</text>

      <text class="display" x="474" y="652" font-size="12.5" fill="#cc9f76" text-anchor="middle" letter-spacing="2">TN MOONSHINE</text>
      <text class="sans" x="474" y="663" font-size="4.8" fill="#cc9f76" text-anchor="middle" font-weight="500" letter-spacing="1">— SPIRITS DISTILLED FROM GRAIN &amp; CANE —</text>
    </g>
  </defs>

  <!-- overall width -->
  <line class="dim-line" x1="107" y1="298" x2="1044" y2="298" marker-start="url(#chevron)" marker-end="url(#chevron)"/>
  <line class="dim-line" x1="107" y1="292" x2="107" y2="358"/>
  <line class="dim-line" x1="1044" y1="292" x2="1044" y2="800"/>
  <rect x="528" y="280" width="72" height="36" fill="#fff"/>
  <text class="dim-text" x="564" y="312" font-size="31" text-anchor="middle">41<tspan font-size="19" dy="-12">3</tspan><tspan font-size="19" dy="12">⁄8</tspan></text>

  <text class="lead-edge" x="561" y="357" text-anchor="middle">LEAD EDGE</text>

  <!-- flaps -->
  <rect class="kraft cut" x="107" y="369" width="176" height="92"/>
  <rect class="kraft cut" x="564" y="369" width="175" height="92"/>
  <rect class="kraft cut" x="107" y="683" width="176" height="92"/>
  <rect class="kraft cut" x="291" y="683" width="265" height="92"/>
  <rect class="kraft cut" x="564" y="683" width="175" height="92"/>
  <rect class="kraft cut" x="746" y="683" width="266" height="92"/>

  <!-- glue tab -->
  <polygon class="kraft cut" points="1015,461 1044,468 1044,675 1015,683"/>

  <!-- end panel -->
  <rect class="ink" x="105" y="461" width="182" height="222"/>
  <text class="sans" x="195" y="499" font-size="5.5" fill="#cc9f76" text-anchor="middle" letter-spacing="0.6">CRAFTED IN MILLBROOK, TN</text>
  <text class="name" x="195" y="577" font-size="15" fill="#cc9f76" text-anchor="middle" letter-spacing="1">COPPER HOLLOW</text>
  <rect class="kraft" x="192" y="640" width="6" height="6"/>
  <text class="condensed" x="195" y="657" font-size="6" fill="#cc9f76" text-anchor="middle" font-weight="400">@RIDGEBACK DISTILLING CO.</text>

  <!-- front panels -->
  <use href="#front-panel"/>
  <use href="#front-panel" x="456"/>

  <!-- side panel -->
  <rect x="560" y="461" width="183" height="222" fill="url(#woodgrain)" role="img" aria-label="Hand-drawn wood grain pattern"/>
  <rect class="ink" x="560" y="624" width="183" height="54"/>
  <polygon class="ink" points="564,462 590,462 590,543 577,536 564,543"/>
  <path d="M574 484 V473 M571 476 L574 472 L577 476 M581 484 V473 M578 476 L581 472 L584 476" stroke="#cc9f76" stroke-width="1" fill="none"/>
  <text class="condensed" x="577" y="492" font-size="6" fill="#cc9f76" text-anchor="middle" font-weight="400">OPEN</text>
  <circle cx="577" cy="502" r="4" fill="none" stroke="#cc9f76" stroke-width="1"/>
  <path d="M573 512 H581 L577 518 Z M577 518 V525 M574 525 H580" stroke="#cc9f76" stroke-width="1" fill="none"/>

  <rect class="ink" x="597" y="485" width="109" height="170"/>
  <rect x="600" y="488" width="103" height="164" fill="none" stroke="#cc9f76" stroke-width="0.6"/>
  <text class="name" x="651" y="499" font-size="6.5" fill="#cc9f76" text-anchor="middle" letter-spacing="0.5">COPPER HOLLOW</text>
  <line x1="603" y1="633" x2="652" y2="633" stroke="#cc9f76" stroke-width="1" stroke-dasharray="0.6 1.6"/>
  <line x1="603" y1="650" x2="652" y2="650" stroke="#cc9f76" stroke-width="1" stroke-dasharray="0.6 1.6"/>
  <g class="condensed" font-size="2.6" fill="#cc9f76" text-anchor="middle" font-weight="400">
    <text x="627" y="638">DISTILLED &amp; BOTTLED BY:</text>
    <text x="627" y="642">HARLAN SPIRITS</text>
    <text x="627" y="646">MILLBROOK, TENNESSEE</text>
  </g>
  <rect class="kraft" x="655" y="631" width="44" height="20"/>
  <text class="condensed" x="651" y="667" font-size="6" fill="#cc9f76" text-anchor="middle" font-weight="400">WWW.RIDGEBACKDISTILLING.COM</text>

  <!-- fold lines -->
  <path class="fold" d="M287 461 H1015 M287 683 H1015 M287 461 V683 M560 461 V683 M743 461 V683 M1015 461 V683"/>

  <!-- left dimensions -->
  <g class="dim-line">
    <line x1="69" y1="369" x2="100" y2="369"/>
    <line x1="69" y1="461" x2="100" y2="461"/>
    <line x1="69" y1="683" x2="100" y2="683"/>
    <line x1="69" y1="775" x2="100" y2="775"/>
    <line x1="73" y1="369" x2="73" y2="461" marker-start="url(#chevron)" marker-end="url(#chevron)"/>
    <line x1="73" y1="461" x2="73" y2="683" marker-start="url(#chevron)" marker-end="url(#chevron)"/>
    <line x1="73" y1="683" x2="73" y2="775" marker-start="url(#chevron)" marker-end="url(#chevron)"/>
  </g>
  <rect x="54" y="402" width="40" height="24" fill="#fff"/>
  <text class="dim-text" x="73" y="423" font-size="19" text-anchor="middle">4<tspan font-size="11" dy="-7">1</tspan><tspan font-size="11" dy="7">⁄16</tspan></text>
  <rect x="50" y="560" width="46" height="24" fill="#fff"/>
  <text class="dim-text" x="73" y="581" font-size="19" text-anchor="middle">9<tspan font-size="11" dy="-7">13</tspan><tspan font-size="11" dy="7">⁄16</tspan></text>
  <rect x="54" y="718" width="40" height="24" fill="#fff"/>
  <text class="dim-text" x="73" y="738" font-size="19" text-anchor="middle">4<tspan font-size="11" dy="-7">1</tspan><tspan font-size="11" dy="7">⁄16</tspan></text>

  <!-- bottom dimensions -->
  <g class="dim-line">
    <line x1="107" y1="783" x2="107" y2="820"/>
    <line x1="287" y1="690" x2="287" y2="820"/>
    <line x1="560" y1="690" x2="560" y2="820"/>
    <line x1="743" y1="690" x2="743" y2="820"/>
    <line x1="1015" y1="690" x2="1015" y2="820"/>
    <line x1="107" y1="815" x2="287" y2="815" marker-start="url(#chevron)" marker-end="url(#chevron)"/>
    <line x1="287" y1="815" x2="560" y2="815" marker-start="url(#chevron)" marker-end="url(#chevron)"/>
    <line x1="560" y1="815" x2="743" y2="815" marker-start="url(#chevron)" marker-end="url(#chevron)"/>
    <line x1="743" y1="815" x2="1015" y2="815" marker-start="url(#chevron)" marker-end="url(#chevron)"/>
    <line x1="975" y1="795" x2="1015" y2="795" marker-end="url(#chevron)"/>
    <line x1="1077" y1="795" x2="1044" y2="795" marker-end="url(#chevron)"/>
  </g>
  <rect x="172" y="803" width="52" height="24" fill="#fff"/>
  <text class="dim-text" x="197" y="824" font-size="20" text-anchor="middle">7<tspan font-size="12" dy="-7">15</tspan><tspan font-size="12" dy="7">⁄16</tspan></text>
  <rect x="397" y="803" width="54" height="24" fill="#fff"/>
  <text class="dim-text" x="424" y="824" font-size="20" text-anchor="middle">12<tspan font-size="12" dy="-7">1</tspan><tspan font-size="12" dy="7">⁄16</tspan></text>
  <rect x="629" y="803" width="44" height="24" fill="#fff"/>
  <text class="dim-text" x="651" y="824" font-size="20" text-anchor="middle">8<tspan font-size="12" dy="-7">1</tspan><tspan font-size="12" dy="7">⁄16</tspan></text>
  <rect x="852" y="803" width="54" height="24" fill="#fff"/>
  <text class="dim-text" x="879" y="824" font-size="20" text-anchor="middle">12<tspan font-size="12" dy="-7">1</tspan><tspan font-size="12" dy="7">⁄16</tspan></text>
  <text class="dim-text" x="956" y="802" font-size="19" text-anchor="middle">1<tspan font-size="11" dy="-7">1</tspan><tspan font-size="11" dy="7">⁄4</tspan></text>

  <!-- right dimensions -->
  <g class="dim-line">
    <line x1="1023" y1="369" x2="1115" y2="369"/>
    <line x1="1023" y1="775" x2="1115" y2="775"/>
    <line x1="1110" y1="369" x2="1110" y2="560" marker-start="url(#chevron)"/>
    <line x1="1110" y1="602" x2="1110" y2="775" marker-end="url(#chevron)"/>
  </g>
  <text class="dim-text" x="1110" y="594" font-size="31" text-anchor="middle">17<tspan font-size="18" dy="-12">15</tspan><tspan font-size="18" dy="12">⁄16</tspan></text>
  <text class="dim-text" x="0" y="0" font-size="17" text-anchor="middle" transform="translate(1078 450) rotate(-90)">&lt;&lt;&lt;&lt;CORR&gt;&gt;&gt;&gt;</text>
</svg>

<p class="story"><strong>COPPER HOLLOW</strong> Working in the hills of Tennessee, we set out to make a shine that goes down easy. No harsh burn, no grimace, just clean grain and cane. Heeding the ways of the old timers who came before us, we run a slow distillation on an all copper pot still, the way it was done back in the hollow. The result is a spirit worth writing home about, and one we're proud to share with you and yours. So crack open a jar of Copper Hollow and enjoy it one glorious sip at a time!</p>
<p class="warning"><strong>GOVERNMENT WARNING:</strong> (1) ACCORDING TO THE SURGEON GENERAL, WOMEN SHOULD NOT DRINK ALCOHOLIC BEVERAGES DURING PREGNANCY BECAUSE OF THE RISK OF BIRTH DEFECTS. (2) CONSUMPTION OF ALCOHOLIC BEVERAGES IMPAIRS YOUR ABILITY TO DRIVE A CAR OR OPERATE MACHINERY, AND MAY CAUSE HEALTH PROBLEMS.</p>
</body>
</html>
```